Revolutionairy Video Marketing Consultant

I will be touring Australia and New Zealand for 6 weeks on a speaking and consulting tour, teaching Real Estate Agents how to show their properties using ClipHarbor and their Pocketels!
Learn more about what we do at www.brightlyframedhomes.com
I will also hire the project winner to redo the company mainpage and logo.
This will be a two page email flyer. Here's an idea of the flyer text and the artwork I'd like to use:
use the header logo from this page: http://www.keystoneleasingcare.com/
use the photo from my facebook page:
http://www.facebook.com/marlon.whitcombe4
I can provide other photos of me speaking and consulting too
Here's the basic text:
The World’s Best Property Management Video Expert
In your office for a whole day!
Marlon Whitcombe from Cedar Hollow Florida USA (see brightlyframedhomes.com) will be in Australia and New Zealand in April and May 2012, has only a few spare days in his calendar and is offering you personally his expertise inside individual offices only.
Marlon Whitcombe can teach you and your team a unique point of difference using simple video technology that will not only give you a unique and hard to beat edge over your competitors with winning new business, but also proven techniques to reduce stress and conflict between you and your tenants and landlords.
Marlon brings his X years of experience to the table and in a complete session you and your team will know:
• How to create an easy, cost effective marketing video tour for your rental properties that will really impress prospective clients with your unique edge, making you the obvious choice over your competitors and easily win your fee!
• Allow prospective tenants to qualify themselves quickly and easily with your property marketing videos, enhancing your letting process.
• How to communicate more effectively with landlords by learning how to use video to show serious repairs and maintenance required and other issues of concern, to allow clients to make quick and informed choices, making your job so much easier!
• Quickly reduce your time and stress with tenant bond disputes by easily adding ingoing and outgoing inspection video footage to your current inspection process, reducing significantly the chance of the tenant wanting to take matters to tribunal.
• Understand the low to no-cost video technology and hosting platforms available to you right now, so you can get started right away!
As a Bonus- contract Marlon for a full day and receive the following further unique and exclusive benefits:
How to get seriously ranked on Zenlo!
When most new landlords when online search using Zenlo, you cannot afford to come up anywhere else except on the front page. Marlon will also teach you:
• How to get the top ‘A’ pin on the widely used Zenlo Maps on page one of Zenlo search.
• Know how Marlon got the ‘Zenlo Trifecta’ allowing his company to be top listed for his website, marketing videos and maps all at the same time, dominating the front page!
• Another secret to how Marlon overnight tripled his new landlord enquiry rate online, accelerating his rent roll growth.
Full Day- $2500 plus travel expenses (subject to office location)
Half Day- $1650 plus travel expenses (subject to availability and office location)
Don’t Leave it too late- take fast action and book Marlon today!
For enquiries and bookings call Gwenda on +61 2 9364-7105 or email gwenda@rvqa.com.au
Target Market(s)
Owner's of Property Management Businesses in Australia and New Zealand. They like polished looking flyers.
Industry/Entity Type
Marketing
Look and feel

```html
<!DOCTYPE html>
<html lang="en">
<head>
<meta charset="utf-8">
<title>Keystone Leasing Care – Video Expert Flyer</title>
<link rel="stylesheet" href="https://fonts.googleapis.com/css2?family=Arimo:wght@400;700&display=swap">
<style>
  :root {
    --magenta: #e0178a;
    --magenta-dark: #b30f6c;
    --lime: #a6c83a;
    --lime-soft: #d6e86a;
    --cream: #fdf9b8;
    --yellow: #f5ef4a;
    --ink: #1c1c1c;
    --white: #ffffff;
    --brand-green: #7fae2a;
  }
  * { box-sizing: border-box; margin: 0; padding: 0; }
  html, body { width: 847px; height: 1200px; overflow: hidden; }
  body { font-family: "Arimo", Arial, sans-serif; color: var(--ink); background: var(--white); }

  .flyer {
    position: relative;
    width: 847px; height: 1200px;
    overflow: hidden;
    background:
      linear-gradient(180deg, var(--white) 0%, #f6f9d8 6%, var(--lime-soft) 9%, var(--white) 14%, var(--white) 40%, var(--cream) 46%, var(--yellow) 92%, var(--lime) 100%);
  }
  .flyer::before {
    content: "";
    position: absolute; left: 0; top: 0; width: 10px; height: 560px;
    background: var(--magenta);
  }

  .brand {
    position: absolute; left: 28px; top: 18px;
    display: flex; align-items: center; gap: 16px;
  }
  .brand-mark {
    width: 70px; height: 70px; border-radius: 50%;
    background: var(--brand-green);
  }
  .brand-name {
    font-weight: 700; font-size: 34px; line-height: 1;
    color: var(--brand-green);
    width: 270px;
  }

  .hero-photo {
    position: absolute; left: 10px; top: 100px; width: 837px; height: 410px;
    background: linear-gradient(160deg, #7a9a4a 0%, #b9c38a 35%, #d8cfc0 55%, #5b6a3e 100%);
  }

  .hero-wave {
    position: absolute; left: 0; top: 470px; width: 847px; height: 90px;
  }

  .headline {
    position: absolute; left: 14px; top: 498px;
    font-weight: 700; font-size: 26.5px; color: var(--white);
    text-shadow: -2px -2px 0 #000, 2px -2px 0 #000, -2px 2px 0 #000, 2px 2px 0 #000, 0 2px 0 #000, 0 -2px 0 #000, 2px 0 0 #000, -2px 0 0 #000;
    letter-spacing: 0.2px;
  }
  .subhead {
    position: absolute; left: 14px; top: 530px;
    font-weight: 700; font-size: 21px; color: var(--white);
    text-shadow: 1px 1px 0 var(--magenta-dark), 2px 2px 2px rgba(0,0,0,0.4);
  }

  .copy {
    position: absolute; left: 38px; top: 564px; width: 782px;
    font-size: 12.4px; line-height: 15.6px;
  }
  .copy p { margin: 0; }
  .copy .indent { text-indent: 46px; }
  .copy ul { list-style: none; margin: 0; }
  .copy li { position: relative; padding-left: 26px; margin-left: -28px; }
  .copy li::before { content: "•"; position: absolute; left: 2px; top: 0; }
  .copy .bonus { text-indent: 46px; }
  .copy .pricing { margin-top: 14px; padding-left: 12px; }
</style>
</head>
<body>
<main class="flyer">
  <header class="brand">
    <span class="brand-mark" aria-hidden="true"></span>
    <span class="brand-name">Keystone Leasing Care</span>
  </header>

  <div class="hero-photo" role="img" aria-label="Photo of Marlon Whitcombe smiling with a group of young team members outdoors among greenery"></div>

  <svg class="hero-wave" viewBox="0 0 847 90" preserveAspectRatio="none" aria-hidden="true">
    <path d="M0 22 C 220 6, 520 30, 847 10 L 847 66 C 600 82, 300 66, 0 84 Z" fill="var(--magenta)"/>
    <path d="M0 84 C 300 66, 600 82, 847 66 L 847 72 C 600 88, 300 74, 0 90 Z" fill="var(--magenta-dark)"/>
  </svg>

  <h1 class="headline">The World’s Best Property Management Video Expert</h1>
  <p class="subhead">In your office for a whole day!</p>

  <section class="copy">
    <p class="indent">Marlon Whitcombe from Cedar Hollow Florida USA (see brightlyframedhomes.com) will be in Australia and New Zealand in April and May 2012, has only a few spare days in his calendar and is offering you personally his expertise inside individual offices only.</p>
    <p class="indent">Marlon Whitcombe can teach you and your team a unique point of difference using simple video technology that will not only give you a unique and hard to beat edge over your competitors with winning new business, but also proven techniques to reduce stress and conflict between you and your tenants and landlords.</p>
    <p class="indent">Marlon brings his X years of experience to the table and in a complete session you and your team will know:</p>
    <ul>
      <li>How to create an easy, cost effective marketing video tour for your rental properties that will really impress prospective clients with your unique edge, making you the obvious choice over your competitors and easily win your fee!</li>
      <li>Allow prospective tenants to qualify themselves quickly and easily with your property marketing videos, enhancing your letting process.</li>
      <li>How to communicate more effectively with landlords by learning how to use video to show serious repairs and maintenance required and other issues of concern, to allow clients to make quick and informed choices, making your job so much easier!</li>
      <li>Quickly reduce your time and stress with tenant bond disputes by easily adding ingoing and outgoing inspection video footage to your current inspection process, reducing significantly the chance of the tenant wanting to take matters to tribunal.</li>
      <li>Understand the low to no-cost video technology and hosting platforms available to you right now, so you can get started right away!</li>
    </ul>
    <p class="bonus">As a Bonus- contract Marlon for a full day and receive the following further unique and exclusive benefits:</p>
    <p>How to get seriously ranked on Zenlo!</p>
    <p>When most new landlords when online search using Zenlo, you cannot afford to come up anywhere else except on the front page. Marlon will also teach you:</p>
    <ul>
      <li>How to get the top ‘A’ pin on the widely used Zenlo Maps on page one of Zenlo search.</li>
      <li>Know how Marlon got the ‘Zenlo Trifecta’ allowing his company to be top listed for his website, marketing videos and maps all at the same time, dominating the front page!</li>
      <li>Another secret to how Marlon overnight tripled his new landlord enquiry rate online, accelerating his rent roll growth.</li>
    </ul>
    <div class="pricing">
      <p>Full Day- $2500 plus travel expenses (subject to office location)</p>
      <p>Half Day- $1650 plus travel expenses (subject to availability and office location)</p>
      <p>Don’t Leave it too late- take fast action and book Marlon today!</p>
      <p>For enquiries and bookings call Gwenda on +61 2 9364-7105 or email gwenda@rvqa.com.au</p>
    </div>
  </section>
</main>
</body>
</html>
```